CONTACT US Page and design for website

We need a contact us page for our website. We would like it to have a message area, a map, our information, etc.

Please see the text attachment for what we are looking for. We need to have something that is creative and interesting, modern and professional.

We believe that a contact US page should be very creative because everyone clicks that to contact us. We want it to be super professional, attention grabbing, pleasing to the eye.

PLEASE KEEP THE HEADER AND FOOTER THE SAME, ONLY THE ACTUAL CONTACT US PAGE NEEDS TO BE WORKED ON. THANKS!
We are excited to work with designers for this project.

Target Market(s)

Clients in technology business

Industry/Entity Type

Information Technology

Number of Pages Required

1 page

Font styles to use
Serif

Requirements
Must have
• CHECK THE TEXT ATTACHMENT PLEASE
• Must stay within our design colors and theme.
Nice to have
• see attachment
Should not have
• it should be special

```html
<!DOCTYPE html>
<html lang="en">
<head>
<meta charset="utf-8">
<title>Contact Us – Korvane Tech</title>
<link href="https://fonts.googleapis.com/css2?family=Arimo:wght@400;700&display=swap" rel="stylesheet">
<style>
:root{
  --teal:#3dbcb0;
  --teal-band:#35b3ad;
  --teal-head:#3aa6b0;
  --ink:#333;
  --muted:#666;
  --line:#e6e6e6;
  --page:#f7f7f7;
  --foot:#a7a7a7;
  --foot-dark:#939393;
  --white:#fff;
}
*{box-sizing:border-box;margin:0;padding:0}
html,body{width:730px;height:1200px;overflow:hidden}
body{position:relative;background:var(--page);font-family:"Arimo",Arial,sans-serif;color:var(--ink)}
.abs{position:absolute}

/* header */
.site-header{position:absolute;left:0;top:0;width:730px;height:93px;background:var(--white)}
.brand{left:38px;top:12px;display:flex;align-items:center;gap:8px}
.brand-mark{width:34px;height:34px;border-radius:50%;background:var(--teal)}
.brand-name{font-size:26px;color:var(--teal);letter-spacing:3px;font-weight:400}
.brand-tag{left:101px;top:38px;font-size:6px;letter-spacing:3.4px;color:var(--teal)}
.account-pill{left:576px;top:0;width:117px;height:19px;border-radius:0 0 14px 14px;background:#b9b9b9;display:flex;font-size:7px;color:#444;overflow:hidden}
.account-pill span{flex:1;display:flex;align-items:center;justify-content:center}
.account-pill span+span{background:#cfcfcf}
.round-icon{width:26px;height:26px;border-radius:50%;border:1px solid #ddd;display:flex;align-items:center;justify-content:center;background:var(--white)}
.chat{left:507px;top:28px}
.chat-label{left:540px;top:37px;font-size:9px;color:#555}
.call{left:592px;top:28px}
.call-number{left:626px;top:34px;font-size:12px;color:#333}
.header-rule{left:0;top:61px;width:730px;height:1px;background:var(--line)}
.main-nav{left:38px;top:71px;display:flex;gap:16px;font-size:7px;letter-spacing:.3px;color:#444}
.search{left:566px;top:69px;width:100px;height:19px;border:1px solid #ccc;border-radius:10px;font-size:7px;color:#444;padding:5px 0 0 13px}
.search svg{position:absolute;right:7px;top:4px}
.cart{left:672px;top:66px;width:24px;height:24px}
.crumb-band{left:0;top:93px;width:730px;height:21px;background:linear-gradient(90deg,var(--teal-band),#45cfc0)}
.crumb{left:80px;top:100px;font-size:7px;color:var(--white);font-weight:700;letter-spacing:.3px}

/* contact card */
.contact-card{left:91px;top:135px;width:547px;height:503px;background:var(--white);border:1px solid #eee}
.split-v{left:365px;top:135px;width:1px;height:503px;background:var(--line)}
.split-h{left:91px;top:386px;width:547px;height:1px;background:var(--line)}
.section-title{font-size:13px;color:var(--teal-head);text-align:center;width:270px}
.field{left:134px;width:188px;height:18px;border:1px solid #ccc;border-radius:2px;font-size:7px;color:#888;padding:4px 6px}
.submit{left:134px;top:326px;width:38px;height:19px;background:var(--teal);color:var(--white);font-size:7px;border-radius:2px;display:flex;align-items:center;justify-content:center}
.hq-box{left:422px;top:192px;width:160px;height:91px;background:#fafafa;border:1px solid #eee;text-align:center;font-size:7px;color:#333;padding-top:20px;line-height:20px}
.hq-box strong{font-weight:400;font-size:9.5px;display:block;line-height:12px;margin-bottom:1px}
.stay-title{left:366px;top:315px;width:272px;text-align:center;font-size:13px;color:#555}
.social-dot{width:12px;height:12px;border-radius:50%;background:var(--teal);top:350px}
.hours{left:104px;top:446px;font-size:7.5px;color:#333;line-height:20.5px}
.hours b{font-weight:700}
.hours svg{vertical-align:-1px;margin-right:2px}
.hours-note{left:104px;top:557px;width:245px;font-size:7px;line-height:15px;color:#444}
.info-grid{left:374px;top:442px;width:252px;height:176px;border:1px solid #eee;display:grid;grid-template-columns:1fr 1fr;grid-template-rows:1fr 1fr}
.info-cell{border:1px solid #f0f0f0;padding:18px 0 0 13px;font-size:7px;color:#333}
.info-cell h3{font-weight:400;font-size:9.5px;margin-bottom:7px}
.info-cell p{margin-bottom:10px;display:flex;align-items:center;gap:3px}

/* map */
.map-area{left:91px;top:661px;width:548px;height:213px;background:linear-gradient(135deg,#ececec,#e2e2e2)}

/* footer */
.site-footer{left:0;top:901px;width:730px;height:189px;background:var(--foot);color:var(--white)}
.footer-about{left:220px;top:915px;width:322px;text-align:center;font-size:8.5px;line-height:12.5px;color:var(--white)}
.footer-rule{left:222px;top:978px;width:286px;height:1px;background:linear-gradient(90deg,transparent,#c8c8c8,transparent)}
.footer-contact{top:993px;font-size:8.5px;color:var(--white);display:flex;gap:5px;line-height:12.5px}
.footer-nav{left:177px;top:1033px;display:flex;gap:14px;font-size:10px;color:var(--white)}
.support-links{left:474px;top:1049px;width:66px;text-align:center;font-size:5.5px;font-weight:700;line-height:9px;color:var(--white)}
.footer-base{left:0;top:1090px;width:730px;height:110px;background:var(--foot-dark)}
.social-ring{top:1102px;width:24px;height:24px;border:1px solid #cfcfcf;border-radius:50%}
.base-rule{left:114px;top:1140px;width:525px;height:1px;background:#aaa}
.base-brand{left:334px;top:1151px;display:flex;gap:6px;align-items:center;font-size:8px;color:var(--white);line-height:11px}
.base-brand i{width:12px;height:12px;border-radius:50%;background:#ddd;display:block}
</style>
</head>
<body>

<header class="site-header">
  <div class="abs brand"><span class="brand-mark"></span><span class="brand-name">KORVANE</span></div>
  <div class="abs brand-tag">SYSTEMS BUILT TO LAST</div>
  <div class="abs account-pill"><span>SIGN UP</span><span>LOGIN</span></div>
  <div class="abs round-icon chat">
    <svg width="12" height="11" viewBox="0 0 12 11"><path d="M1 1h10v6H5l-3 3V7H1z" fill="var(--teal)"/></svg>
  </div>
  <div class="abs chat-label">LIVE CHAT</div>
  <div class="abs round-icon call">
    <svg width="11" height="11" viewBox="0 0 12 12"><path d="M3 1l2 3-1 1c1 2 2 3 3 3l1-1 3 2-1 2C6 11 1 6 1 2z" fill="var(--teal)"/></svg>
  </div>
  <div class="abs call-number">555-014-2290</div>
  <div class="abs header-rule"></div>
  <nav class="abs main-nav">
    <span>SERVERS</span><span>WORKSTATIONS</span><span>COMPONENTS</span><span>VIRTUAL REALITY</span><span>DRONES</span><span>ABOUT US</span><span>BLOG</span><span>RESOURCES</span><span>CONTACT US</span>
  </nav>
  <div class="abs search">Search
    <svg width="10" height="10" viewBox="0 0 10 10"><circle cx="4" cy="4" r="3" fill="none" stroke="var(--teal)" stroke-width="1.4"/><path d="M6.3 6.3L9 9" stroke="var(--teal)" stroke-width="1.6"/></svg>
  </div>
  <div class="abs round-icon cart">
    <svg width="12" height="10" viewBox="0 0 12 10"><path d="M1 2h10l-1 6H2z" fill="none" stroke="var(--teal)" stroke-width="1.3"/><path d="M4 2V1h4v1" stroke="var(--teal)" fill="none"/></svg>
  </div>
</header>
<div class="abs crumb-band"></div>
<div class="abs crumb">HOME <span style="font-weight:400">/</span> CONTACT US</div>

<main>
  <div class="abs contact-card"></div>
  <div class="abs split-v"></div>
  <div class="abs split-h"></div>

  <h2 class="abs section-title" style="left:94px;top:159px">Get an Enquiry</h2>
  <div class="abs field" style="top:200px">Full Name</div>
  <div class="abs field" style="top:229px">Email ID</div>
  <div class="abs field" style="top:258px">Contact Number</div>
  <div class="abs field" style="top:287px">Message</div>
  <div class="abs submit">Submit</div>

  <h2 class="abs section-title" style="left:367px;top:158px">Office Headquarter</h2>
  <address class="abs hq-box" style="font-style:normal">
    <strong>Korvane Tech, LLC</strong>2150 Linden Avenue,<br>Cedar Ridge, CA 90417
  </address>
  <h2 class="abs stay-title">Stay Connected</h2>
  <span class="abs social-dot" style="left:428px" aria-label="Social profile"></span>
  <span class="abs social-dot" style="left:471px" aria-label="Social profile"></span>
  <span class="abs social-dot" style="left:516px" aria-label="Social profile"></span>
  <span class="abs social-dot" style="left:562px" aria-label="Social profile"></span>

  <h2 class="abs section-title" style="left:94px;top:409px">Hours of Operation</h2>
  <div class="abs hours">
    <div><svg width="7" height="7" viewBox="0 0 8 8"><circle cx="4" cy="4" r="3.3" fill="none" stroke="var(--teal)"/><path d="M4 2v2h2" stroke="var(--teal)" fill="none"/></svg><b>Monday</b> : 8:00am- 5:00pm</div>
    <div><svg width="7" height="7" viewBox="0 0 8 8"><circle cx="4" cy="4" r="3.3" fill="none" stroke="var(--teal)"/><path d="M4 2v2h2" stroke="var(--teal)" fill="none"/></svg><b>Tuesday</b> : 8:00am- 5:00pm</div>
    <div><svg width="7" height="7" viewBox="0 0 8 8"><circle cx="4" cy="4" r="3.3" fill="none" stroke="var(--teal)"/><path d="M4 2v2h2" stroke="var(--teal)" fill="none"/></svg><b>Wednesday</b> : 8:00am- 5:00pm</div>
    <div><svg width="7" height="7" viewBox="0 0 8 8"><circle cx="4" cy="4" r="3.3" fill="none" stroke="var(--teal)"/><path d="M4 2v2h2" stroke="var(--teal)" fill="none"/></svg><b>Thursday</b> : 8:00am- 5:00pm</div>
    <div><svg width="7" height="7" viewBox="0 0 8 8"><circle cx="4" cy="4" r="3.3" fill="none" stroke="var(--teal)"/><path d="M4 2v2h2" stroke="var(--teal)" fill="none"/></svg><b>Friday</b> : 8:00am- 5:00pm</div>
  </div>
  <p class="abs hours-note">Our dedicated customer service representatives are available 24/7 by phone</p>

  <h2 class="abs section-title" style="left:367px;top:409px">Contact Information</h2>
  <div class="abs info-grid">
    <div class="info-cell"><h3>General Inquiries</h3>
      <p><svg width="6" height="6" viewBox="0 0 12 12"><path d="M3 1l2 3-1 1c1 2 2 3 3 3l1-1 3 2-1 2C6 11 1 6 1 2z" fill="var(--teal)"/></svg>(555)014-2290</p>
      <p><svg width="7" height="5" viewBox="0 0 8 6"><rect width="8" height="6" fill="var(--teal)"/><path d="M0 0l4 3 4-3" stroke="#fff" fill="none" stroke-width=".8"/></svg>info@korvanetech.com</p></div>
    <div class="info-cell"><h3>Sales Inquiries</h3>
      <p><svg width="6" height="6" viewBox="0 0 12 12"><path d="M3 1l2 3-1 1c1 2 2 3 3 3l1-1 3 2-1 2C6 11 1 6 1 2z" fill="var(--teal)"/></svg>(555)014-2290</p>
      <p><svg width="7" height="5" viewBox="0 0 8 6"><rect width="8" height="6" fill="var(--teal)"/><path d="M0 0l4 3 4-3" stroke="#fff" fill="none" stroke-width=".8"/></svg>sales@korvanetech.com</p></div>
    <div class="info-cell"><h3>Purchase Inquiries</h3>
      <p><svg width="6" height="6" viewBox="0 0 12 12"><path d="M3 1l2 3-1 1c1 2 2 3 3 3l1-1 3 2-1 2C6 11 1 6 1 2z" fill="var(--teal)"/></svg>(555)014-2291</p>
      <p><svg width="7" height="5" viewBox="0 0 8 6"><rect width="8" height="6" fill="var(--teal)"/><path d="M0 0l4 3 4-3" stroke="#fff" fill="none" stroke-width=".8"/></svg>purchasing@korvanetech.com</p></div>
    <div class="info-cell"><h3>HR Inquiries</h3>
      <p><svg width="6" height="6" viewBox="0 0 12 12"><path d="M3 1l2 3-1 1c1 2 2 3 3 3l1-1 3 2-1 2C6 11 1 6 1 2z" fill="var(--teal)"/></svg>(555)014-2290</p>
      <p><svg width="7" height="5" viewBox="0 0 8 6"><rect width="8" height="6" fill="var(--teal)"/><path d="M0 0l4 3 4-3" stroke="#fff" fill="none" stroke-width=".8"/></svg>hr@korvanetech.com</p></div>
  </div>

  <div class="abs map-area" role="img" aria-label="Street map showing the Korvane Tech office location with a place card"></div>
</main>

<footer>
  <div class="abs site-footer"></div>
  <p class="abs footer-about">Based in Cedar Ridge California, Korvane Tech offers custom servers, storage, and workstations for local businesses in Los Angeles, Beverly Hills, Thousand Oaks, Ventura, Orange County, Santa Barbara, Oxnard, Irvine, Anaheim, and San Diego. Korvane Tech also offers such products to clients throughout the United States and Worldwide.</p>
  <div class="abs footer-rule"></div>
  <div class="abs footer-contact" style="left:222px">
    <svg width="7" height="10" viewBox="0 0 7 10"><path d="M3.5 0A3.5 3.5 0 0 0 0 3.5C0 6 3.5 10 3.5 10S7 6 7 3.5A3.5 3.5 0 0 0 3.5 0z" fill="#fff"/><circle cx="3.5" cy="3.5" r="1.3" fill="var(--foot)"/></svg>
    <span>2150 Linden Ave.<br>Cedar Ridge, CA 90417</span>
  </div>
  <div class="abs footer-contact" style="left:332px">
    <svg width="8" height="8" viewBox="0 0 12 12" style="margin-top:2px"><path d="M3 1l2 3-1 1c1 2 2 3 3 3l1-1 3 2-1 2C6 11 1 6 1 2z" fill="#fff"/></svg>
    <span>555-014-2290</span>
  </div>
  <div class="abs footer-contact" style="left:430px">
    <svg width="9" height="7" viewBox="0 0 8 6" style="margin-top:3px"><rect width="8" height="6" fill="#fff"/><path d="M0 0l4 3 4-3" stroke="var(--foot)" fill="none" stroke-width=".8"/></svg>
    <span>sales@korvanetech.com</span>
  </div>
  <nav class="abs footer-nav">
    <span>Computer Hardware</span><span>Drones</span><span>Virtual Reality</span><span>About Us</span><span>Customer Support</span>
  </nav>
  <div class="abs support-links">Terms and Conditions<br>Warranty Information<br>Contact Us<br>Return Policy</div>
  <div class="abs footer-base"></div>
  <span class="abs social-ring" style="left:298px" aria-label="Social profile"></span>
  <span class="abs social-ring" style="left:330px" aria-label="Social profile"></span>
  <span class="abs social-ring" style="left:363px" aria-label="Social profile"></span>
  <span class="abs social-ring" style="left:396px" aria-label="Social profile"></span>
  <div class="abs base-rule"></div>
  <div class="abs base-brand"><i></i><span>Korvane Tech, LLC.<br>Copyright © 2017</span></div>
</footer>

</body>
</html>
```